Flyer Advertisement Design

Flyer dimensions 4" x 6"

Simple design with logo and additional info. On the front of the flyer:

- place the logo at the top
- beneath the logo add the website and phone number
- simple less is more approach
- feel free to add your own personal touch

On the back:

- Requirements
- Perfect for Birthdays and Anniversaries
- Rentals available hourly, daily, and weekly
- Group Rentals available at discounted rates
- Enter to win a free rental - url and QR code

Target Market(s)

Rental customer

Industry/Entity Type

Car Rental

Font styles to use
Serif
Sans Serif

Colors

Designer to choose colors to be used in the design.

Requirements
Must have
• FRONT:
• Please include our phone number and website:
• 555-271-8640
• www.MarrowbyTrikeHire.com
• BACK:
• REQUIREMENTS
• At least 25 years of age
• Valid Driver's License
• Debit or Credit Card
• Must know how to drive a manual transmission or stick shift

```html
<!DOCTYPE html>
<html lang="en">
<head>
<meta charset="utf-8">
<title>Marrowby Trike Hire – Flyer</title>
<link href="https://fonts.googleapis.com/css2?family=Open+Sans:wght@600;700;800&display=swap" rel="stylesheet">
<style>
  :root {
    --backdrop: #e9e6e1;
    --paper: #ffffff;
    --ink: #1c1c1e;
    --brand-blue: #1a7fd0;
    --brand-blue-deep: #0f5fb0;
    --night: #1e2733;
    --night-deep: #141b24;
    --sketch-grey: #b9c1c6;
    --text-light: #ffffff;
  }
  * { margin: 0; padding: 0; box-sizing: border-box; }
  html, body { width: 1200px; height: 1200px; overflow: hidden; }
  body {
    background: var(--backdrop);
    font-family: "Open Sans", sans-serif;
    position: relative;
  }
  .flyer {
    position: absolute;
    top: 208px;
    width: 523px;
    height: 784px;
    overflow: hidden;
  }
  .flyer--front { left: 52px; background: var(--paper); }
  .flyer--back { left: 627px; background: var(--night); }

  /* Front */
  .hero-art {
    position: absolute;
    left: 30px; top: 57px;
    width: 460px; height: 385px;
    border-radius: 50%;
    background: radial-gradient(ellipse at 50% 50%, #2a4a73 0%, #3b6fa8 30%, var(--sketch-grey) 60%, #eef1f3 80%, transparent 100%);
  }
  .brand-name {
    position: absolute;
    left: 0; right: 0; top: 478px;
    text-align: center;
    font-weight: 800;
    font-size: 36px;
    letter-spacing: 2px;
    text-transform: uppercase;
    color: var(--ink);
  }
  .divider-band {
    position: absolute;
    left: 0; right: 0; top: 592px;
    height: 11px;
    background: var(--ink);
  }
  .contact-panel {
    position: absolute;
    left: 0; right: 0; top: 603px; bottom: 0;
    background: linear-gradient(135deg, var(--brand-blue) 0%, var(--brand-blue-deep) 60%, var(--brand-blue) 100%);
    color: var(--text-light);
    text-align: center;
  }
  .contact-phone {
    position: absolute;
    left: 0; right: 0; top: 26px;
    font-weight: 700;
    font-size: 74px;
    line-height: 1;
    letter-spacing: -2px;
    text-shadow: 2px 2px 0 rgba(0,0,0,0.35);
  }
  .contact-rule {
    position: absolute;
    left: 28px; right: 28px; top: 110px;
    height: 3px;
    background: var(--text-light);
  }
  .contact-web {
    position: absolute;
    left: 0; right: 0; top: 118px;
    font-weight: 700;
    font-size: 22px;
    text-shadow: 1px 1px 0 rgba(0,0,0,0.4);
  }

  /* Back */
  .back-photo {
    position: absolute; inset: 0;
    background: linear-gradient(160deg, var(--night-deep) 0%, #263246 45%, #2c3a52 65%, var(--night-deep) 100%);
  }
  .perks { position: absolute; left: 0; top: 0; width: 100%; height: 100%; list-style: none; }
  .perk {
    position: absolute;
    left: 67px;
    font-weight: 700;
    font-size: 25px;
    line-height: 31px;
    color: var(--text-light);
  }
  .perk::before {
    content: "";
    position: absolute;
    left: -18px; top: 12px;
    width: 10px; height: 10px;
    border-radius: 50%;
    background: var(--brand-blue);
  }
  .req-heading {
    position: absolute;
    left: 44px; top: 404px;
    width: 289px; height: 51px;
    background: var(--brand-blue);
    color: var(--text-light);
    font-weight: 700;
    font-size: 32px;
    line-height: 51px;
    text-align: center;
  }
  .requirements { list-style: none; }
  .requirement {
    position: absolute;
    left: 70px;
    font-weight: 700;
    font-size: 25px;
    line-height: 31px;
    color: var(--text-light);
  }
  .tick {
    position: absolute;
    left: -28px; top: -16px;
    width: 34px; height: 40px;
  }
</style>
</head>
<body>

<section class="flyer flyer--front">
  <div class="hero-art" role="img" aria-label="Sketched illustration of a blue and black three-wheeled roadster over grey brush strokes"></div>
  <div class="brand-name">Marrowby Trike Hire</div>
  <div class="divider-band"></div>
  <div class="contact-panel">
    <div class="contact-phone">555-271-8640</div>
    <div class="contact-rule"></div>
    <div class="contact-web">www.MarrowbyTrikeHire.com</div>
  </div>
</section>

<section class="flyer flyer--back">
  <div class="back-photo" role="img" aria-label="Dark photo of a three-wheeled roadster parked on asphalt"></div>
  <ul class="perks">
    <li class="perk" style="top:33px">Perfect for Birthdays<br>and Anniversaries</li>
    <li class="perk" style="top:124px">Rentals available hourly,<br>daily, and weekly</li>
    <li class="perk" style="top:215px">Group Rentals available<br>at discounted rates</li>
    <li class="perk" style="top:307px">Enter to win a free rental<br>url and QR code</li>
  </ul>
  <div class="req-heading">REQUIREMENTS</div>
  <ul class="requirements">
    <li class="requirement" style="top:475px"><svg class="tick" viewBox="0 0 34 40"><path d="M2 26 L10 36 L32 2 L10 28 Z" fill="var(--brand-blue)"/></svg>At least 25 years of age</li>
    <li class="requirement" style="top:536px"><svg class="tick" viewBox="0 0 34 40"><path d="M2 26 L10 36 L32 2 L10 28 Z" fill="var(--brand-blue)"/></svg>Valid Driver's License</li>
    <li class="requirement" style="top:596px"><svg class="tick" viewBox="0 0 34 40"><path d="M2 26 L10 36 L32 2 L10 28 Z" fill="var(--brand-blue)"/></svg>Debit or Credit Card</li>
    <li class="requirement" style="top:658px"><svg class="tick" viewBox="0 0 34 40"><path d="M2 26 L10 36 L32 2 L10 28 Z" fill="var(--brand-blue)"/></svg>Must know how to drive a<br>manual transmission<br>or stick shift</li>
  </ul>
</section>

</body>
</html>
```